Falcon Ridge pipe restorations recruiting business card

We need a recruiting business card for our commercial pipe line company “Falcon Ridge” that reaches out to individuals looking for a job or who would be a great fit to our team. We want to include:
- Recognizing the candidates potential
—> You are amazing!
- Capture who we are (name, subtitle, tag line & our core values)
—> FALCON RIDGE, Pipe Restoration Solutions, INVESTIGATE | PLAN | DELIVER | , our values: Family, Integrity, Generosity, Faith, Humility, Communication, Collaboration, Innovation, Mission Minded, Positivity, Improvement, Fulfillment, Fun and Diversity
3. Call to action (apply at website/email this address/call this number to become apart of our team/family)
—> If you are interested in a career with a fully funded startup that is using technology and a new and innovative approach to the age old art of plumbing we are seeking team members who appreciate hard work and want to be part of a winning team!
—> send your resume to: recruiting@falconridgepipe.example
4. Personal point of reference (let them know x [person handing out card writes their name] sent you! )
—> Let them know that _______________ sent you!
Call me if you have any questions _________________

Contact Information for Business Card

Front: Explaining who we are/core values
Back: recruitment explanation

Font styles to use
Serif
Sans Serif

```html
<!DOCTYPE html>
<html lang="en">
<head>
<meta charset="utf-8">
<title>Falcon Ridge – Recruiting Business Card</title>
<link rel="stylesheet" href="https://fonts.googleapis.com/css2?family=Open+Sans:wght@400;600;700&display=swap">
<style>
  :root {
    --ink: #1d1d1d;
    --paper: #ffffff;
    --card-dark: #1e1e1e;
    --stage: #e6e7e9;
    --muted: #555555;
    --rule: #d9d9d9;
  }
  * { box-sizing: border-box; margin: 0; padding: 0; }
  html, body {
    width: 1200px; height: 900px; overflow: hidden;
    background: var(--stage);
    font-family: "Open Sans", Arial, sans-serif;
  }
  .sheet {
    width: 1200px; height: 900px;
    display: flex; flex-direction: column; align-items: center; justify-content: center;
    gap: 36px;
  }
  .card {
    width: 700px; height: 400px; position: relative; overflow: hidden;
    box-shadow: 0 6px 18px rgba(0,0,0,.18);
  }

  /* Front */
  .card--front { background: var(--paper); color: var(--ink); }
  .front-intro { position: absolute; left: 40px; top: 44px; width: 620px; }
  .front-name { font-size: 26px; font-weight: 700; letter-spacing: .5px; }
  .front-subtitle { font-size: 18px; font-weight: 600; color: var(--muted); margin-top: 4px; }
  .brand-lockup {
    position: absolute; right: 40px; top: 40px; text-align: right;
  }
  .brand-row { display: flex; align-items: center; justify-content: flex-end; gap: 10px; }
  .brand-dot { width: 46px; height: 46px; border-radius: 50%; background: var(--ink); }
  .brand-name { font-size: 34px; font-weight: 400; letter-spacing: 1px; color: var(--ink); line-height: 1; }
  .brand-line { font-size: 11px; letter-spacing: 1.6px; color: var(--muted); margin-top: 3px; }
  .core-values {
    position: absolute; left: 40px; top: 168px; width: 620px;
    font-size: 15px; font-weight: 600; line-height: 1.5; color: #333;
  }
  .core-values strong { font-weight: 700; color: var(--ink); }
  .tagline-band {
    position: absolute; left: 0; right: 0; bottom: 34px; height: 52px;
    background: var(--card-dark); color: var(--paper);
    display: flex; align-items: center; justify-content: center; gap: 34px;
    font-size: 20px; font-weight: 700; letter-spacing: 1.5px;
  }

  /* Back */
  .card--back { background: var(--card-dark); color: var(--paper); }
  .back-heading {
    position: absolute; left: 0; right: 0; top: 36px; text-align: center;
    font-size: 24px; font-weight: 700; text-decoration: underline; text-underline-offset: 4px;
  }
  .back-pitch {
    position: absolute; left: 50px; right: 50px; top: 92px; text-align: center;
    font-size: 15px; line-height: 1.6; color: #e8e8e8;
  }
  .back-resume {
    position: absolute; left: 50px; right: 50px; top: 210px; text-align: center;
    font-size: 15px; color: #dcdcdc;
  }
  .back-resume strong { color: var(--paper); font-weight: 700; }
  .back-referral {
    position: absolute; left: 50px; top: 254px; font-size: 15px; font-weight: 600;
    display: flex; align-items: flex-end; gap: 10px;
  }
  .referral-blank { display: inline-block; width: 200px; border-bottom: 2px solid var(--paper); height: 18px; }
  .contact-band {
    position: absolute; left: 0; right: 0; bottom: 30px; height: 44px;
    background: var(--paper); color: var(--ink);
    display: flex; align-items: center; justify-content: space-between; padding: 0 30px;
    font-size: 15px;
  }
  .contact-band strong { font-weight: 700; font-size: 17px; }
</style>
</head>
<body>
<main class="sheet">

  <section class="card card--front" aria-label="Card front">
    <div class="front-intro">
      <h1 class="front-name">FALCON RIDGE</h1>
      <p class="front-subtitle">Pipe Restoration Solutions</p>
    </div>
    <div class="brand-lockup">
      <div class="brand-row">
        <span class="brand-dot"></span>
        <span class="brand-name">FALCON RIDGE</span>
      </div>
      <p class="brand-line">PIPE RESTORATION SOLUTIONS</p>
      <p class="brand-line">INVESTIGATE • PLAN • DELIVER</p>
    </div>
    <p class="core-values"><strong>Core Values:</strong> Family, Integrity, Generosity, Faith, Humility, Communication, Collaboration, Innovation, Mission Minded, Positivity, Improvement, Fulfillment, Fun and Diversity</p>
    <div class="tagline-band">
      <span>Investigate</span><span>•</span><span>Plan</span><span>•</span><span>Deliver</span>
    </div>
  </section>

  <section class="card card--back" aria-label="Card back">
    <h2 class="back-heading">Get Ready to Become a Part of Our Team !</h2>
    <p class="back-pitch">If you are interested in a career with a fully funded startup that is using technology and a new and innovative approach to the age old art of plumbing we are seeking team members who appreciate hard work and want to be part of a winning team!</p>
    <p class="back-resume">Send your resume to: <strong>recruiting@falconridgepipe.example</strong></p>
    <p class="back-referral"><span>* Let them know that</span><span class="referral-blank"></span><span>has sent you</span></p>
    <div class="contact-band">
      <span>For more info, call: <strong>123 456 7890</strong></span>
      <span>Visit: <strong>www.falconridgepipe.example</strong></span>
    </div>
  </section>

</main>
</body>
</html>
```